LH Business Card NEEDED

Lumen Harbour is a finance brokering company that provide lending advise to consumer, business, corporate, and property developer for all their financing needs.

We source and match customer needs in Home Loan, Business Loan, Commercial Property Loan, Assets Finance, and other banking related services. It is a market with full of loans! But we specialise in more complex loan structure and our client base are more business and corporate level. Our suppliers are Banks and large Financial Institution where these business card will go to.

We have a great deal of Asian clients, therefore the card need to also include Chinese language together with English.

Refer to attached file for logo and content requirements.

We are looking for designs with the following ingredients:
* Innovative & Creative
* Professional
* Trust & Security

Please pick colours that will compliment the colours of the company logo.

Please provide a unique design, for example the edge of the card is rounded or corner cut off.
Updates

Company logo uploaded.

Please commence submitting your design.

Target Market(s)

Target audiences are businessmen, corporate, and property developer. And also a great deal of Chinese clients.

Industry/Entity Type

Finance

Contact Information for Business Card

Lumen Harbour Pty. Ltd.
Morris Okafor
Director
Suite 42, 7-9 Pellow St. Dunmore NSW 2738

Requirements
Must have
• Double sided design

```html
<!DOCTYPE html>
<html lang="en">
<head>
<meta charset="utf-8">
<title>Lumen Harbour — Business Card</title>
<link rel="stylesheet" href="https://fonts.googleapis.com/css2?family=Cormorant+Garamond:wght@400;600;700&family=Noto+Serif+TC:wght@400;600&display=swap">
<style>
  :root {
    --stage: #ece8e2;
    --card-white: #ffffff;
    --brown-deep: #3f2210;
    --brown-mid: #6a3d1c;
    --brown-warm: #8a5a2a;
    --gold: #b8963e;
    --gold-light: #e6d39a;
    --silver: #9a9a9a;
    --ink: #2b2b2b;
    --cream: #f3e6c8;
  }
  * { box-sizing: border-box; margin: 0; padding: 0; }
  html, body { width: 1200px; height: 1024px; overflow: hidden; }
  body {
    background: var(--stage);
    font-family: "Cormorant Garamond", "Noto Serif TC", serif;
    color: var(--ink);
    display: flex;
    flex-direction: column;
    align-items: center;
    justify-content: center;
    gap: 44px;
  }
  .card {
    position: relative;
    width: 760px;
    height: 442px;
    border-radius: 34px;
    overflow: hidden;
    box-shadow: 0 6px 18px rgba(0,0,0,.18);
  }

  /* ---------- Front ---------- */
  .card-front { background: var(--card-white); }
  .front-swoosh { position: absolute; inset: 0; }
  .brand-lockup {
    position: absolute;
    left: 70px; top: 82px;
    display: flex; align-items: center; gap: 20px;
  }
  .brand-dot {
    width: 70px; height: 70px; border-radius: 50%;
    background: var(--silver);
    flex: none;
  }
  .brand-text { display: flex; flex-direction: column; }
  .brand-name {
    font-weight: 600; font-size: 20px; letter-spacing: 6px;
    text-transform: uppercase; color: var(--ink);
    white-space: nowrap;
  }
  .brand-name-zh {
    font-family: "Noto Serif TC", serif; font-weight: 600;
    font-size: 22px; letter-spacing: 5px; margin-top: 4px;
    color: var(--ink);
  }
  .brand-rule {
    width: 230px; height: 1px; background: var(--silver);
    margin-top: 8px;
  }
  .person {
    position: absolute; left: 70px; bottom: 60px;
  }
  .person-name {
    font-weight: 700; font-size: 32px; color: var(--gold);
    white-space: nowrap;
  }
  .person-name-zh, .person-role-zh {
    font-family: "Noto Serif TC", serif; font-size: 14px; color: var(--ink);
  }
  .person-role { font-weight: 700; font-size: 19px; margin-top: 2px; }
  .contact {
    position: absolute; right: 40px; top: 44px;
    text-align: right; color: var(--cream);
    font-size: 16px; line-height: 1.75;
  }
  .contact-row { display: flex; align-items: center; justify-content: flex-end; gap: 9px; white-space: nowrap; }
  .contact-row svg { width: 14px; height: 14px; fill: var(--cream); flex: none; }
  .address { font-size: 14px; line-height: 1.6; margin-top: 4px; color: var(--cream); white-space: nowrap; }
  .contact-web { position: absolute; right: 40px; bottom: 40px; color: var(--cream); font-size: 17px; }

  /* ---------- Back ---------- */
  .card-back {
    background: linear-gradient(120deg, var(--brown-deep) 0%, var(--brown-mid) 45%, var(--brown-warm) 65%, var(--brown-deep) 100%);
    display: flex; flex-direction: column; align-items: center; justify-content: center;
  }
  .back-lockup { display: flex; align-items: center; gap: 26px; margin-top: -30px; }
  .back-dot { width: 120px; height: 120px; border-radius: 50%; background: var(--silver); flex: none; }
  .back-name {
    font-weight: 600; font-size: 42px; letter-spacing: 9px;
    text-transform: uppercase; color: var(--gold-light); white-space: nowrap;
  }
  .back-name-zh {
    font-family: "Noto Serif TC", serif; font-weight: 600;
    font-size: 36px; letter-spacing: 8px; color: var(--gold-light);
  }
  .back-web {
    position: absolute; bottom: 44px; left: 0; right: 0;
    text-align: center; color: var(--cream); font-size: 19px; letter-spacing: 1px;
  }
</style>
</head>
<body>

<section class="card card-front" aria-label="Business card front">
  <svg class="front-swoosh" viewBox="0 0 760 442" preserveAspectRatio="none" aria-hidden="true">
    <defs>
      <linearGradient id="frontBrown" x1="0" y1="0" x2="1" y2="1">
        <stop offset="0" stop-color="#3f2210"/>
        <stop offset=".55" stop-color="#7a4b22"/>
        <stop offset="1" stop-color="#3f2210"/>
      </linearGradient>
      <linearGradient id="goldBand" x1="0" y1="0" x2="1" y2="0">
        <stop offset="0" stop-color="#e6d39a"/>
        <stop offset=".5" stop-color="#b8963e"/>
        <stop offset="1" stop-color="#f5eac6"/>
      </linearGradient>
    </defs>
    <path d="M760 0 L470 0 C430 150 420 300 370 442 L760 442 Z" fill="url(#goldBand)"/>
    <path d="M760 0 L495 0 C455 150 450 300 400 442 L760 442 Z" fill="url(#frontBrown)"/>
    <line x1="395" y1="200" x2="395" y2="290" stroke="#b8963e" stroke-width="2"/>
  </svg>

  <div class="brand-lockup">
    <div class="brand-dot"></div>
    <div class="brand-text">
      <span class="brand-name">Lumen Harbour</span>
      <span class="brand-name-zh">明港通</span>
      <span class="brand-rule"></span>
    </div>
  </div>

  <div class="person">
    <p class="person-name">Morris Okafor</p>
    <p class="person-name-zh">莫立思</p>
    <p class="person-role">Director</p>
    <p class="person-role-zh">董事</p>
  </div>

  <div class="contact">
    <p class="contact-row">000-000-0000
      <svg viewBox="0 0 24 24"><path d="M6.6 10.8a15 15 0 0 0 6.6 6.6l2.2-2.2a1 1 0 0 1 1-.25 11.4 11.4 0 0 0 3.6.57 1 1 0 0 1 1 1V20a1 1 0 0 1-1 1A17 17 0 0 1 3 4a1 1 0 0 1 1-1h3.5a1 1 0 0 1 1 1c0 1.25.2 2.45.57 3.57a1 1 0 0 1-.25 1z"/></svg>
    </p>
    <p class="contact-row">name@domainname.com
      <svg viewBox="0 0 24 24"><path d="M2 5h20v14H2z M2 5l10 8 10-8" stroke="#3f2210" stroke-width="1.5"/></svg>
    </p>
    <p class="address">Suite 42, 7-9 Pellow St.<br>Dunmore NSW 2738</p>
  </div>
  <p class="contact-web">www.websitename.com</p>
</section>

<section class="card card-back" aria-label="Business card back">
  <div class="back-lockup">
    <div class="back-dot"></div>
    <div>
      <p class="back-name">Lumen Harbour</p>
      <p class="back-name-zh">明港通</p>
    </div>
  </div>
  <p class="back-web">www.websitename.com</p>
</section>

</body>
</html>
```